Create lumora book cover: Paper Lanterns

I need a cover designed for my book
Title is “Paper Lanterns”
Tag line is “ A Ledger of Quiet Seasons“

With the words “ A handbook on how to remove yourself from your company“ somewhere on the page.

Author name “Corin Maddox”

The cover will be used on lumora and paper back and needs to comply with all LPS formatting rules.

Target Market(s)

Small Business owners

Font styles to use
Serif

```html
<!DOCTYPE html>
<html lang="en">
<head>
<meta charset="utf-8">
<title>Paper Lanterns — Corin Maddox</title>
<link rel="stylesheet" href="https://fonts.googleapis.com/css2?family=Bebas+Neue&family=Raleway:wght@300;400;700&family=Oswald:wght@700&display=swap">
<style>
  :root {
    --backdrop: #222222;
    --cover-black: #0a0a0a;
    --white: #ffffff;
    --sun-yellow: #f2d813;
    --flame-light: #ffb347;
    --flame-mid: #e0651a;
    --flame-deep: #8a2206;
    --rule-gold: #c9ad12;
  }
  * { margin: 0; padding: 0; box-sizing: border-box; }
  html, body {
    width: 1200px;
    height: 1200px;
    overflow: hidden;
    background: var(--backdrop);
  }
  .cover {
    position: absolute;
    left: 227px;
    top: 40px;
    width: 746px;
    height: 1120px;
    background: var(--cover-black);
    overflow: hidden;
  }
  .title-top {
    position: absolute;
    top: 110px;
    left: 0;
    width: 100%;
    text-align: center;
    font-family: "Bebas Neue", sans-serif;
    font-size: 128px;
    line-height: 1;
    letter-spacing: 0.42em;
    padding-left: 0.42em;
    color: var(--white);
  }
  .title-main {
    position: absolute;
    top: 235px;
    left: 0;
    width: 100%;
    text-align: center;
    font-family: "Bebas Neue", sans-serif;
    font-size: 212px;
    line-height: 1;
    letter-spacing: 0.01em;
    background: linear-gradient(180deg, var(--flame-light) 0%, var(--flame-mid) 45%, var(--flame-deep) 100%);
    -webkit-background-clip: text;
    background-clip: text;
    color: transparent;
    -webkit-text-stroke: 2px var(--white);
  }
  .sun-scene {
    position: absolute;
    top: 470px;
    left: 118px;
    width: 530px;
    height: 530px;
    border-radius: 50%;
    background: linear-gradient(180deg, var(--sun-yellow) 0%, var(--sun-yellow) 55%, var(--cover-black) 74%);
  }
  .tagline-block {
    position: absolute;
    top: 835px;
    left: 290px;
    width: 340px;
    text-align: center;
    font-family: "Raleway", sans-serif;
    color: var(--white);
  }
  .tagline-lead {
    font-weight: 300;
    font-size: 32px;
    line-height: 1.1;
  }
  .tagline-accent {
    font-weight: 700;
    font-size: 34px;
    line-height: 1.1;
    letter-spacing: 0.03em;
    color: var(--sun-yellow);
  }
  .rule {
    height: 2px;
    background: var(--rule-gold);
    margin: 8px 0;
  }
  .handbook-line {
    font-weight: 400;
    font-size: 20px;
    line-height: 1.2;
  }
  .author {
    position: absolute;
    top: 1025px;
    left: 270px;
    width: 380px;
    text-align: center;
    font-family: "Oswald", sans-serif;
    font-weight: 700;
    font-size: 36px;
    letter-spacing: 0.22em;
    color: var(--white);
  }
</style>
</head>
<body>
  <main class="cover">
    <h1 class="book-title">
      <span class="title-top">PAPER</span>
      <span class="title-main">LANTERNS</span>
    </h1>

    <div class="sun-scene" role="img" aria-label="Silhouette of a lone figure standing atop a mountain path against a large yellow sun"></div>

    <div class="tagline-block">
      <p class="tagline-lead">A Ledger of<br>Quiet</p>
      <p class="tagline-accent">SEASONS</p>
      <div class="rule"></div>
      <p class="handbook-line">A handbook on how to remove<br>yourself from your company</p>
      <div class="rule"></div>
    </div>

    <p class="author">CORIN MADDOX</p>
  </main>
</body>
</html>
```